LOCAL TAXI SERVICE NEEDS A BANNER AD DESIGN

NEED BANNER AD DESIGN FOR TAXI SERVICE IN NJ. WE PROVIDE LOCAL AND LONG DISTANCE TRANSPORTATION. OUR MAIN BASE OF CUSTOMER GO TO THE MAJOR AIRPORTS IN THE TRI STATE AREA. I WANT TO OFFER A SPECIAL GOING TO HOLMBRIDGE AIRPORT OF $35.00 WITH A COUPON CODE OF PW 12. THIS BANNER AD WILL BE USED FOR MY PALWIRE PAGE

Target Market(s)

PEOPLE WHO TRAVEL A LOT

Industry/Entity Type

Taxi

Font styles to use
Serif
Sans Serif

Colors
0792cd
0255a3
33a6d7
85cae6
cee9f5
ecf7fb
ffffff

Requirements
Must have
• MY COMPANY NAME: DORVAN'S TAXI

```html
<!DOCTYPE html>
<html lang="en">
<head>
<meta charset="utf-8">
<title>Dorvan's Taxi – Holmbridge Airport Special</title>
<link rel="stylesheet" href="https://fonts.googleapis.com/css2?family=Didact+Gothic&family=Roboto:wght@400;500&display=swap">
<style>
  :root {
    --stage: #e9e9ea;
    --night: #05070d;
    --deep-blue: #0a1fa8;
    --royal-blue: #1436d6;
    --bright-blue: #2f57f0;
    --pale-blue: #a9b8f2;
    --ink: #000000;
    --white: #ffffff;
    --lavender: #c9cdf2;
  }
  * { margin: 0; padding: 0; box-sizing: border-box; }
  html, body {
    width: 1200px; height: 838px; overflow: hidden;
    background: var(--stage);
  }
  .banner {
    position: absolute; left: 220px; top: 39px;
    width: 760px; height: 760px; overflow: hidden;
    font-family: "Didact Gothic", "Century Gothic", sans-serif;
    color: var(--white);
  }
  .backdrop {
    position: absolute; inset: 0;
    background:
      linear-gradient(135deg, transparent 0 52%, rgba(47,87,240,.55) 52% 60%, transparent 60% 100%),
      linear-gradient(135deg, transparent 0 66%, rgba(20,54,214,.6) 66% 76%, transparent 76% 100%),
      linear-gradient(100deg, var(--night) 0%, #0b1440 28%, var(--royal-blue) 58%, var(--bright-blue) 75%, var(--pale-blue) 100%);
  }
  .backdrop::after {
    content: ""; position: absolute; inset: 0;
    background: linear-gradient(to bottom, rgba(0,0,0,0) 55%, rgba(0,0,0,.55) 100%);
  }
  .brand {
    position: absolute; left: 2px; top: 26px;
    width: 350px; height: 68px;
    display: flex; align-items: center; gap: 12px;
    padding-left: 5px;
    background: var(--royal-blue);
  }
  .brand-mark {
    width: 52px; height: 56px;
    border: 2px solid var(--white);
    flex: none;
  }
  .brand-name {
    font-size: 38px; letter-spacing: -1px; white-space: nowrap;
    color: var(--white);
  }
  .vehicle {
    position: absolute; left: 99px; top: 100px;
    width: 555px; height: 270px;
    border-radius: 120px 140px 40px 60px;
    background: radial-gradient(ellipse at 55% 45%, #ffffff 0%, #eef0f4 55%, #c8ccd6 80%, rgba(200,204,214,0) 100%);
  }
  .chevrons {
    position: absolute; left: 151px; top: 392px;
    width: 180px; height: 125px;
  }
  .offer {
    position: absolute; left: 344px; top: 384px;
    font-size: 40px; line-height: 48px;
    text-transform: uppercase;
  }
  .offer .lead { font-size: 36px; }
  .price-box {
    position: absolute; left: 126px; top: 552px;
    width: 369px; height: 125px;
    background: var(--deep-blue);
    display: flex; align-items: center; justify-content: center;
  }
  .price {
    font-family: "Roboto", Arial, sans-serif; font-weight: 400;
    font-size: 104px; letter-spacing: -3px; line-height: 1;
    background: linear-gradient(to bottom, var(--white) 30%, var(--lavender) 100%);
    -webkit-background-clip: text; background-clip: text; color: transparent;
  }
  .coupon {
    position: absolute; left: 495px; top: 552px;
    width: 156px; height: 125px;
    background: var(--ink);
    text-align: center;
  }
  .coupon-label {
    margin-top: 14px;
    font-family: "Roboto", Arial, sans-serif; font-size: 16px; letter-spacing: .5px;
  }
  .coupon-code {
    margin-top: 4px;
    font-family: "Roboto", Arial, sans-serif; font-size: 58px; letter-spacing: -2px;
  }
</style>
</head>
<body>
  <section class="banner">
    <div class="backdrop" role="img" aria-label="Steel bridge at dusk washed in blue with diagonal light bands"></div>

    <header class="brand">
      <span class="brand-mark"></span>
      <span class="brand-name">DORVAN'S TAXI</span>
    </header>

    <div class="vehicle" role="img" aria-label="White minivan taxi shown from the front three-quarter view"></div>

    <svg class="chevrons" viewBox="0 0 180 125" aria-hidden="true">
      <defs>
        <linearGradient id="chevron-fill" x1="0" y1="0" x2="0" y2="1">
          <stop offset="0" stop-color="#ffffff"/>
          <stop offset="1" stop-color="#b9bff0"/>
        </linearGradient>
      </defs>
      <polygon points="0,0 48,0 110,62 48,125 0,125 62,62" fill="url(#chevron-fill)"/>
      <polygon points="70,0 118,0 180,62 118,125 70,125 132,62" fill="url(#chevron-fill)"/>
    </svg>

    <h1 class="offer">
      <span class="lead">Special going</span><br>
      to Holmbridge<br>
      Airport
    </h1>

    <div class="price-box"><span class="price">$35.00</span></div>
    <div class="coupon">
      <p class="coupon-label">COUPON CODE</p>
      <p class="coupon-code">PW12</p>
    </div>
  </section>
</body>
</html>
```